Logo + Business Card Design Project

We are looking at changing our logo and reprinting business cards.

Attached is a design concept for the logo (we have no hi res files for this).

The logo needs to be able to work standalone without the tagline.

We are happy for you to use this concept or design a new one. The existing concept is quite well liked.

We would also consider not having Solutions in the logo and just have QRV Systems Pty Ltd in the body text of the card.

We have a Tag Line that needs to go on all documentation / websites etc wherever the logo appears.

Tagline: Lifting work higher

Our message to clients is that we have solutions that:

QRV Systems:
Lifting work higher

Turning up Revenue
Turning up Profit
Turning up Confidence

We would require the files in a High Res format for print and a scalable transparent format for web.
(We also need greyscale and monochrome files)
All source files need to be delivered with existing layers etc

A corporate guide with the logo usage and colours should be specified.

Suggestions:
The new logo has to have CMYK colours of 100 90 0 0

CMYK 100 90 0 0
RGB #21409A
Websafe #224499
Greyscale #414141

We would also need a business card layout designed.
Could be one sided or 2 sided. Will probably print matt cello 2 sides on 350gsm gloss
Updates

Industry/Entity Type

Business

Requirements
Should not have
• Lower case n in QRV.

```html
<!DOCTYPE html>
<html lang="en">
<head>
<meta charset="utf-8">
<title>QRV Systems – Business Card &amp; Logo</title>
<link rel="stylesheet" href="https://fonts.googleapis.com/css2?family=Open+Sans:wght@400;600;700;800&family=PT+Sans+Narrow&family=Petit+Formal+Script&display=swap">
<style>
  :root {
    --brand-blue: #21409a;
    --stage: #1f1f1f;
    --paper: #ffffff;
    --ink: #1a1a1a;
    --ghost: #e4e4e4;
    --rule: #333333;
  }
  * { margin: 0; padding: 0; box-sizing: border-box; }
  html, body { width: 849px; height: 1200px; overflow: hidden; }
  body { background: var(--stage); position: relative; font-family: "Open Sans", sans-serif; }

  .card {
    position: absolute;
    width: 355px; height: 217px;
    background: var(--paper);
    overflow: hidden;
  }
  .card--front { left: 112px; top: 190px; z-index: 2; }
  .card--back { left: 350px; top: 397px; z-index: 1; }

  .wordmark {
    font-family: "Open Sans", sans-serif;
    font-weight: 800;
    line-height: 1;
    white-space: nowrap;
  }
  .card--front .wordmark {
    position: absolute; left: 20px; top: 24px;
    font-size: 84px; letter-spacing: 30px; color: var(--brand-blue);
  }
  .front-band { position: absolute; inset: 0; }
  .tagline {
    position: absolute; left: 32px; top: 150px;
    font-family: "Petit Formal Script", cursive;
    font-size: 15px; color: var(--ink);
    white-space: nowrap;
  }
  .holder {
    position: absolute; right: 18px; top: 162px;
    text-align: right; color: var(--paper);
  }
  .holder__name { font-weight: 700; font-size: 12.5px; line-height: 1.3; }
  .holder__role { font-size: 11px; line-height: 1.3; }

  .card--back .wordmark {
    position: absolute; left: 2px; top: -26px;
    font-size: 118px; letter-spacing: 30px; color: var(--ghost);
  }
  .contact {
    position: absolute; top: 142px;
    font-family: "PT Sans Narrow", sans-serif;
    font-size: 10px; line-height: 13.5px; color: var(--ink);
    display: grid; grid-template-columns: auto auto; column-gap: 18px;
  }
  .contact--phones { left: 17px; }
  .contact--web { left: 170px; }
  .contact-divider {
    position: absolute; left: 155px; top: 120px; width: 1px; height: 97px;
    background: var(--rule);
  }

  .mono-panel { position: absolute; left: 0; top: 0; }
  .logo-reversed, .logo-mono {
    position: absolute; top: 930px; font-size: 80px; letter-spacing: 26px;
  }
  .logo-reversed { left: 112px; color: var(--paper); }
  .logo-mono { left: 500px; color: #000; }
</style>
</head>
<body>

  <section class="card card--front" aria-label="Business card front">
    <svg class="front-band" width="355" height="217" viewBox="0 0 355 217" aria-hidden="true">
      <path d="M70 217 Q190 128 355 120 L355 217 Z" fill="var(--brand-blue)"/>
    </svg>
    <div class="wordmark">QRV</div>
    <p class="tagline">Lifting work higher</p>
    <div class="holder">
      <p class="holder__name">Daniel Verrow</p>
      <p class="holder__role">Project Director</p>
    </div>
  </section>

  <section class="card card--back" aria-label="Business card back">
    <div class="wordmark" aria-hidden="true">QRV</div>
    <div class="contact contact--phones">
      <span>Phone</span><span>+61 2 5550-0100</span>
      <span>Support</span><span>+61 2 5550-0133</span>
      <span>Fax</span><span>+61 2 5550-0101</span>
      <span>Mobile</span><span>0400 555 018</span>
    </div>
    <div class="contact-divider"></div>
    <div class="contact contact--web">
      <span>Email</span><span>daniel.verrow@qrv.com.au</span>
      <span>Web</span><span>www.qrv.com.au</span>
      <span>Address</span><span>118/42 Harlow Street</span>
      <span></span><span>Northbridge NSW 2063</span>
    </div>
  </section>

  <svg class="mono-panel" width="849" height="1200" viewBox="0 0 849 1200" aria-hidden="true">
    <polygon points="452,858 849,825 849,1133 425,1063" fill="var(--paper)"/>
  </svg>
  <div class="wordmark logo-reversed">QRV</div>
  <div class="wordmark logo-mono">QRV</div>

</body>
</html>
```